business card for training & coaching company, Brightwell.co

Create a warm, clean, professional 2-sided business card for Brightwell.co.
Brightwell.co is a new company that shares Brightwell Dialogue (combination of mindfulness, kindness, and nonviolent communication), training and coaching individuals and groups.
Include the logo provided, perhaps incorporating a second opaque version of it as well.
Feelings & Needs lists on the reverse side of the card.

Target Market(s)

Women 30-60 years old, university educated.
Spiritual, may be Buddhist.

Industry/Entity Type

Training

Contact Information for Business Card

Jessamine T. Holloway, MSc
Group Facilitator & Certified Wellness Coach
Brightwell Dialogue training & support
Group Facilitator & Coach
01482 936 555
07754 608 219
www.brightwell.co

Font styles to use
Sans Serif

Requirements
Must have
• Front -- Contact details, logo provided.
• Back -- Feelings list; Needs list
• Professional yet warm, inviting, friendly feel.
Nice to have
• little graphics (telephone for phone number, envelope for email, globe for web);
• Clean font (like Sathu, Frutiga, Helvetica).
• Feeling of movement or transformation.
Should not have
• More than 3 colours.
• Loud or busy designs.
• A gentle curve or two is ok, but not swirly designs.
• No black or other heavy backgrounds.

```html
<!DOCTYPE html>
<html lang="en">
<head>
<meta charset="utf-8">
<title>Brightwell.co business card</title>
<link href="https://fonts.googleapis.com/css2?family=Open+Sans:wght@400;600;700&display=swap" rel="stylesheet">
<style>
  :root {
    --backdrop: #c9c9c9;
    --card: #fdf8f2;
    --card-warm: #fbeee0;
    --orange: #f28a1c;
    --orange-deep: #d9691a;
    --ink: #3a3330;
    --ink-soft: #6b615b;
  }
  * { box-sizing: border-box; margin: 0; padding: 0; }
  html, body { width: 1200px; height: 852px; overflow: hidden; }
  body {
    background: var(--backdrop);
    font-family: "Open Sans", Arial, sans-serif;
    position: relative;
  }
  .card {
    position: absolute;
    top: 271px;
    width: 540px;
    height: 309px;
    border-radius: 14px;
    background: linear-gradient(120deg, var(--card) 0%, var(--card) 45%, var(--card-warm) 100%);
    color: var(--ink);
    overflow: hidden;
    box-shadow: 0 2px 6px rgba(0, 0, 0, 0.12);
  }
  .card--back { left: 40px; }
  .card--front { left: 620px; border-bottom: 5px solid var(--orange); }

  .list-title {
    color: var(--orange-deep);
    font-weight: 700;
    font-size: 15px;
    letter-spacing: 0.3px;
    margin-bottom: 2px;
  }
  .list { list-style: none; font-size: 15px; line-height: 19.5px; }
  .list-mark { color: var(--orange); font-size: 13px; display: inline-block; width: 14px; }
  .list-mark--blank { visibility: hidden; }

  .feelings { position: absolute; left: 26px; top: 24px; }
  .needs { position: absolute; right: 26px; top: 24px; text-align: right; }
  .needs .list-mark { text-align: right; }

  .brand {
    position: absolute;
    top: 140px;
    display: flex;
    align-items: center;
    gap: 10px;
    color: var(--orange-deep);
    font-weight: 600;
    font-size: 20px;
  }
  .brand-dot {
    width: 18px; height: 18px; border-radius: 50%;
    background: var(--orange);
  }
  .card--back .brand { left: 190px; }
  .card--front .brand { left: 34px; }

  .person { position: absolute; left: 290px; top: 60px; }
  .person-name { color: var(--orange-deep); font-weight: 700; font-size: 17px; }
  .person-role { font-size: 12.5px; line-height: 16px; color: var(--ink-soft); }

  .contacts { position: absolute; left: 290px; top: 168px; list-style: none; }
  .contact {
    display: flex; align-items: center; gap: 10px;
    font-size: 14px; line-height: 20px; color: var(--ink);
  }
  .contact-icon { width: 13px; height: 13px; fill: var(--orange); flex: none; }
</style>
</head>
<body>

<section class="card card--back" aria-label="Card back: feelings and needs">
  <div class="feelings">
    <h2 class="list-title">FEELINGS</h2>
    <ul class="list">
      <li><span class="list-mark">»</span>confusion</li>
      <li><span class="list-mark">»</span>curious</li>
      <li><span class="list-mark">»</span>despair</li>
      <li><span class="list-mark">»</span>edgy</li>
      <li><span class="list-mark">»</span>fiery</li>
      <li><span class="list-mark">»</span>grief</li>
      <li><span class="list-mark">»</span>nervous</li>
      <li><span class="list-mark">»</span>powerless</li>
      <li><span class="list-mark">»</span>shock</li>
      <li><span class="list-mark">»</span>torn</li>
      <li><span class="list-mark">»</span>weary</li>
      <li><span class="list-mark list-mark--blank">»</span>&amp; more..</li>
    </ul>
  </div>

  <div class="brand"><span class="brand-dot"></span>Brightwell.co</div>

  <div class="needs">
    <h2 class="list-title">NEEDS</h2>
    <ul class="list">
      <li>belonging<span class="list-mark">«</span></li>
      <li>choice<span class="list-mark">«</span></li>
      <li>clarity<span class="list-mark">«</span></li>
      <li>empathy<span class="list-mark">«</span></li>
      <li>freedom<span class="list-mark">«</span></li>
      <li>meaning<span class="list-mark">«</span></li>
      <li>mourning<span class="list-mark">«</span></li>
      <li>peace<span class="list-mark">«</span></li>
      <li>safety<span class="list-mark">«</span></li>
      <li>support<span class="list-mark">«</span></li>
      <li>understanding<span class="list-mark">«</span></li>
      <li>&amp; more<span class="list-mark list-mark--blank">«</span></li>
    </ul>
  </div>
</section>

<section class="card card--front" aria-label="Card front: contact details">
  <div class="brand"><span class="brand-dot"></span>Brightwell.co</div>

  <div class="person">
    <h1 class="person-name">Jessamine T. Holloway</h1>
    <p class="person-role">MSc &amp; Certified Wellness Coach</p>
    <p class="person-role">Group Facilitator &amp; Coach</p>
  </div>

  <ul class="contacts">
    <li class="contact">
      <svg class="contact-icon" viewBox="0 0 16 16" aria-hidden="true"><path d="M4 0h8a1 1 0 0 1 1 1v14a1 1 0 0 1-1 1H4a1 1 0 0 1-1-1V1a1 1 0 0 1 1-1zm1 2v10h6V2zm3 11a1 1 0 1 0 0 2 1 1 0 0 0 0-2z"/></svg>
      01482 936 555
    </li>
    <li class="contact">
      <svg class="contact-icon" viewBox="0 0 16 16" aria-hidden="true"><path d="M1 5c0-2 3-3 7-3s7 1 7 3v1h-4V4.5H5V6H1zM3 7h10l1 7H2zm5 1.5a2 2 0 1 0 0 4 2 2 0 0 0 0-4z"/></svg>
      07754 608 219
    </li>
    <li class="contact">
      <svg class="contact-icon" viewBox="0 0 16 16" aria-hidden="true"><path d="M0 3h16v1.2L8 9 0 4.2zm0 2.6 8 4.8 8-4.8V13H0z"/></svg>
      jessamine@brightwell.com
    </li>
    <li class="contact">
      <svg class="contact-icon" viewBox="0 0 16 16" aria-hidden="true"><path d="M8 0a8 8 0 1 0 0 16A8 8 0 0 0 8 0zm-1 2v3H4.3A6 6 0 0 1 7 2zm2 0a6 6 0 0 1 2.7 3H9zM2.2 7H7v2H2.2a6 6 0 0 1 0-2zM9 7h4.8a6 6 0 0 1 0 2H9zm-4.7 4H7v3a6 6 0 0 1-2.7-3zM9 11h2.7A6 6 0 0 1 9 14z"/></svg>
      www.brightwell.co
    </li>
  </ul>
</section>

</body>
</html>
```